Letterhead Design for Law Firm

**Edit: I have added the photo of a bottom that I like.

------
We are looking for a re-design of our new letterhead. The letterhead is for a law firm and will be used for digital and traditionally printed correspondence.

Here are some suggestions:

- Please use colours are #8ec900 and simple black.
- Please do not use any type of "waves" at the bottom of the page. This is not in style at all.
- Please stay modern yet conservative.
- Please use font Segoe UI Light or similar if you can
- Avoid clipart or illustrations.
- Utilize ample white space in the layout so the design looks clean and information is easy to read at a glance. Don't overcrowd the letterhead.
- Make sure the letterhead design is consistent with our brand identity (see brambleford.ca)
-Please, no black headers or footers.

I am attaching my current letterhead and signature for your convenience.

Remember, the letterhead is an extension of our professional identity. We are a successful firm and trial lawyers who correspond with insurers, judges, lawyers, courts, clients, etc. Make it new, modern, attractive, yet powerful and conservative.

It needs to be easily printable. I would like the bleed removed in print so the black bar the bottom crosses the page (but the text is not near the edges)

Target Market(s)

Clients, Government Offices, Judiciary, Lawyers, Insurance Companies, Colleagues.

Industry/Entity Type

Law

Font styles to use
Other font styles liked:
• Segoe UI LIght, Calibri Light,

Colors
00AB8E
00BBA5
67D7C9
C6EFE9
E9F9F6

Requirements
Must have
• Everything that is on the letterhead now.
Nice to have
• Cutting Edge design, yet conservative.
Should not have
• law firm cliche design, images,

```html
<!DOCTYPE html>
<html lang="en">
<head>
<meta charset="utf-8">
<title>Harcourt Letterhead</title>
<link rel="stylesheet" href="https://fonts.googleapis.com/css2?family=Open+Sans:wght@300;400;600;700&display=swap">
<style>
  :root {
    --green: #8ec900;
    --ink: #111111;
    --ink-soft: #2a2a2a;
    --paper: #ffffff;
    --backdrop: #e4e4e4;
  }
  * { margin: 0; padding: 0; box-sizing: border-box; }
  html, body { width: 1200px; height: 1155px; overflow: hidden; }
  body {
    background: var(--backdrop);
    font-family: "Open Sans", "Segoe UI", sans-serif;
    color: var(--ink);
    position: relative;
  }
  .sheet {
    position: absolute;
    left: 165px; top: 15px;
    width: 870px; height: 1125px;
    background: var(--paper);
    overflow: hidden;
  }
  .brand {
    position: absolute; left: 70px; top: 118px;
    width: 400px;
  }
  .brand-name {
    font-size: 28px; font-weight: 400; letter-spacing: 1.5px;
    color: var(--ink); text-transform: uppercase; line-height: 1.25;
  }
  .contact {
    position: absolute; left: 565px; top: 58px;
    border-left: 3px solid var(--green);
    padding: 2px 0 4px 12px;
    font-size: 11.5px; line-height: 15.5px; color: var(--ink-soft);
    font-style: normal;
  }
  .contact b { font-weight: 700; color: var(--ink); }
  .contact .web-accent { color: var(--green); font-weight: 600; }
  .contact .practice { margin-top: 16px; }
  .letter {
    position: absolute; left: 100px; top: 222px;
    font-size: 15px; font-weight: 300; line-height: 22px;
  }
  .letter .strong { font-weight: 600; }
  .letter p { margin-bottom: 16px; }
  .addressee { margin-bottom: 18px; }
  .re-block {
    position: absolute; left: 100px; top: 562px; width: 690px;
    border-bottom: 1px solid var(--ink);
    padding-bottom: 10px;
    font-size: 15px; line-height: 21px;
    display: flex;
  }
  .re-label { font-weight: 600; width: 190px; padding-top: 42px; }
  .re-subject { font-weight: 600; }
  .re-subject sup { font-size: 9px; }
  .signoff {
    position: absolute; left: 140px; top: 858px;
    font-size: 15px; font-weight: 300; line-height: 20px;
  }
  .signoff .firm { font-weight: 400; text-transform: uppercase; }
  .signature {
    display: block; width: 200px; height: 56px; margin: 6px 0 4px;
    background: linear-gradient(90deg, #f2f2f2, #e6e6e6);
  }
  .signoff .name { font-size: 16px; }
  .signoff .corp { font-weight: 600; font-size: 13px; }
  .signoff .small { font-size: 13px; }
  .footer { position: absolute; left: 0; bottom: 0; width: 870px; height: 110px; }
  .footer-url {
    position: absolute; right: 34px; bottom: 40px;
    color: #fff; font-size: 21px; font-weight: 300; letter-spacing: 0.5px;
  }
</style>
</head>
<body>
  <main class="sheet">
    <header>
      <div class="brand">
        <div class="brand-name">Harcourt Personal Injury Lawyers</div>
      </div>
      <address class="contact">
        www.<span class="web-accent">BRAMBLEFORD</span>.ca<br>
        24 Merrow Street W., Suite 910<br>
        Hamilton, ON&nbsp; L8P 0B2<br>
        <b>T:</b> 905-555-0142<br>
        <b>F:</b> 905-555-0187<br>
        <b>File Clerk:</b> Clara Whitmore<br>
        <b>Email:</b> clara@brambleford.ca
        <div class="practice">
          <b>Practice Restricted</b><br>
          Serious Personal Injury<br>
          Wrongful Death Litigation<br>
          Long-Term Disability Litigation<br>
          Wrongful Dismissal Litigation<br>
          Employee Terminations
        </div>
      </address>
    </header>

    <section class="letter">
      <p class="strong">Without Prejudice</p>
      <p>March 13, 2024</p>
      <p class="strong">By Email</p>
      <div class="addressee">
        Northvale Insurance Company<br>
        Claims Litigation Department<br>
        480 Aldergate Road South<br>
        P.O. Box 3100<br>
        Waterloo, ON&nbsp;&nbsp; N2J 0A0
      </div>
      <p>Attention:&nbsp; Mr. Owen Dale</p>
      <p>Mr. Dale:</p>
    </section>

    <div class="re-block">
      <div class="re-label">Re:</div>
      <div class="re-subject">
        Marsh v. Corvell et al.<br>
        DOL:&nbsp; September 12, 2019<br>
        Pre-Mediation Settlement Proposal – March 13<sup>th</sup>, 2024
      </div>
    </div>

    <section class="signoff">
      Yours very truly,<br>
      <span class="firm">Harcourt Personal Injury Lawyers</span>
      <span class="signature" role="img" aria-label="Handwritten signature of Daniel P. Harcourt"></span>
      <span class="name">Daniel P. Harcourt</span><br>
      <span class="corp">Harcourt Law Professional Corporation</span><br>
      <span class="small">/cw</span><br>
      <span class="small">Encl.</span>
    </section>

    <footer class="footer">
      <svg width="870" height="110" viewBox="0 0 870 110" aria-hidden="true">
        <rect x="0" y="88" width="870" height="22" fill="var(--green)"/>
        <polygon points="560,110 580,32 870,32 870,110" fill="var(--paper)"/>
        <polygon points="572,110 592,32 870,32 870,110" fill="var(--green)"/>
      </svg>
      <div class="footer-url">www.brambleford.ca</div>
    </footer>
  </main>
</body>
</html>
```